E-commerce website needs a splash page ad

Our website, tinkerloft.com, needs an additional ad on our 'splash page'. It needs to fit within these dimensions: 980x383 pixels.

Please visit tinkerloft.com to see the slide in action, and to see what content already exists.

The splash ad needs to contain an image of the Dr. Glowfin product we are selling, as well as the Dr Glowfin logo featured in one of the corners of the ad. A button need to be made (visual only) with the text "view page" or something akin to "take me to part of the website that sells this product"

The ad needs to be clean, modern, and aimed towards a mature audience- no flowery graphics are needed.

Target Market(s)

Families, senior citizens, homeowners, small business owners

Industry/Entity Type

Product

Font styles to use
Sans Serif

Colors

Designer to choose colors to be used in the design.

Requirements
Must have
• -Black background with large, white font that says (in one way or another) " outdoor motion detection lighting"
-Dr Glowfin logo must be present in one of the 4 corners
-must fit the 980x383 pixels size
-A light gray-to-white gradient somewhere in the background
- At least 2 Dr. Glowfin images must be used (a white and black dr glowfin, for example)
Nice to have
• -A cone-shaped white gradient emitting from one of the Dr. Glowfin spotlights
- This white gradient will 'illuminate' a "view page" button (or 'buy now', etc)

```html
<!DOCTYPE html>
<html lang="en">
<head>
<meta charset="utf-8">
<title>Dr Glowfin – Outdoor Motion Detection Lighting</title>
<link href="https://fonts.googleapis.com/css2?family=Ubuntu:wght@400;500;700&display=swap" rel="stylesheet">
<style>
  :root {
    --bg-dark: #050506;
    --bg-mid: #2b2d33;
    --bg-light: #6d7079;
    --headline: #ffffff;
    --brand-name: #ffffff;
    --brand-tagline: #c9ccd2;
    --button-top: #f7a13a;
    --button-bottom: #e0640f;
    --product-white-a: #f2f4f6;
    --product-white-b: #aeb3ba;
    --product-dark-a: #4b5560;
    --product-dark-b: #1a1f26;
  }
  * { margin: 0; padding: 0; box-sizing: border-box; }
  html, body {
    width: 1200px; height: 465px; overflow: hidden;
    background: var(--bg-dark);
  }
  .banner {
    position: relative;
    width: 1200px; height: 465px; overflow: hidden;
    font-family: "Ubuntu", sans-serif;
    background:
      radial-gradient(ellipse 720px 300px at 420px 40px, var(--bg-light) 0%, var(--bg-mid) 45%, transparent 100%),
      linear-gradient(180deg, var(--bg-mid) 0%, #111215 60%, var(--bg-dark) 100%);
  }
  .light-cone {
    position: absolute; left: 0; top: 0;
    width: 1200px; height: 465px;
  }
  .product { position: absolute; }
  .product--white {
    left: 0; top: 0; width: 360px; height: 345px;
    border-radius: 0 48% 40% 0 / 0 42% 48% 0;
    background: radial-gradient(ellipse at 45% 35%, var(--product-white-a) 0%, var(--product-white-b) 100%);
  }
  .product--dark {
    left: 985px; top: 18px; width: 200px; height: 345px;
    border-radius: 46% 40% 30% 30% / 40% 40% 30% 30%;
    background: radial-gradient(ellipse at 40% 30%, var(--product-dark-a) 0%, var(--product-dark-b) 100%);
  }
  .headline {
    position: absolute; left: 383px; top: 94px;
    color: var(--headline);
    font-weight: 700;
    font-size: 62px;
    line-height: 70px;
    letter-spacing: 4px;
  }
  .brand {
    position: absolute; left: 82px; top: 368px;
  }
  .brand__name {
    color: var(--brand-name);
    font-weight: 500; font-size: 38px; line-height: 44px;
    letter-spacing: 1px;
  }
  .brand__tagline {
    margin-top: 4px;
    color: var(--brand-tagline);
    font-weight: 400; font-size: 19px; line-height: 24px;
  }
  .cta {
    position: absolute; left: 579px; top: 355px;
    width: 191px; height: 44px;
    display: flex; align-items: center; justify-content: center; gap: 8px;
    border-radius: 3px;
    background: linear-gradient(180deg, var(--button-top), var(--button-bottom));
    box-shadow: 0 2px 4px rgba(0,0,0,0.35);
    color: #fff; font-weight: 700; font-size: 24px;
  }
  .cta svg { width: 12px; height: 18px; }
</style>
</head>
<body>
  <div class="banner">
    <svg class="light-cone" viewBox="0 0 1200 465" aria-hidden="true">
      <defs>
        <linearGradient id="beam" x1="0" y1="0" x2="1" y2="0.2">
          <stop offset="0" stop-color="#ffffff" stop-opacity="0.95"/>
          <stop offset="0.55" stop-color="#e8e9ec" stop-opacity="0.55"/>
          <stop offset="1" stop-color="#cfd1d6" stop-opacity="0"/>
        </linearGradient>
        <filter id="soft" x="-20%" y="-50%" width="140%" height="200%">
          <feGaussianBlur stdDeviation="18"/>
        </filter>
      </defs>
      <polygon points="230,230 250,280 800,430 790,330" fill="url(#beam)" filter="url(#soft)"/>
    </svg>

    <div class="product product--white" role="img" aria-label="White wireless motion-sensor LED spotlight on a wall mount"></div>
    <div class="product product--dark" role="img" aria-label="Dark gray wireless motion-sensor LED spotlight on a wall mount"></div>

    <h1 class="headline">Outdoor<br>Motion Detection<br>Lighting</h1>

    <div class="brand">
      <p class="brand__name">Dr Glowfin</p>
      <p class="brand__tagline">Clear Light Wherever You Need It</p>
    </div>

    <div class="cta">Buy Now
      <svg viewBox="0 0 12 18" aria-hidden="true"><polyline points="2,2 9,9 2,16" fill="none" stroke="#fff" stroke-width="3"/></svg>
    </div>
  </div>
</body>
</html>
```